Postcard Design

Qelvaro is a medical sales and communication network between doctors and doctors, doctors and sales representatives and doctors and medical companies. Doctors offices are off limits to sales reps. Communication takes place on a closed network of computer tablets. Doctors,Companies and Sale Representatives must join the the Qelvaro network and then they begin to send short videos or messages or pdf files to those doctors in their territory. Doctors will post the Qel varo logo on their doors, restricting sales reps from waiting in offices to make cold calls. They receive permission for office visits
through the tablet based platform.

Industry/Entity Type

Communication

```html
<!DOCTYPE html>
<html lang="en">
<head>
<meta charset="utf-8">
<title>Qelvaro – Sales Representative Restricted Office Postcard</title>
<link rel="stylesheet" href="https://fonts.googleapis.com/css2?family=Open+Sans:wdth,wght@75..100,300..800&display=swap">
<style>
  :root {
    --page-bg: #e9ecef;
    --header-navy: #0f3a5e;
    --panel-blue: #2f8fc0;
    --deep-navy: #0a2b49;
    --stripe-blue: #1d79b6;
    --stripe-light: #3aa0d6;
    --text-white: #ffffff;
    --tagline-blue: #9fdcf7;
    --photo-light: #eef1f3;
    --photo-mid: #c9d0d6;
    --photo-shadow: #8e979f;
  }
  * { box-sizing: border-box; margin: 0; padding: 0; }
  html, body {
    width: 1200px;
    height: 976px;
    overflow: hidden;
    background: var(--page-bg);
  }
  .postcard {
    position: absolute;
    left: 40px;
    top: 84px;
    width: 1120px;
    height: 808px;
    overflow: hidden;
    background: var(--panel-blue);
    font-family: "Open Sans", Arial, sans-serif;
    box-shadow: 0 4px 18px rgba(0,0,0,0.18);
  }
  .postcard__photo {
    position: absolute;
    left: 0;
    top: 0;
    width: 534px;
    height: 740px;
    background:
      radial-gradient(ellipse at 55% 45%, var(--photo-light) 0%, var(--photo-mid) 55%, var(--photo-shadow) 100%);
  }
  .postcard__header {
    position: absolute;
    left: 534px;
    top: 0;
    width: 586px;
    height: 144px;
    background: var(--header-navy);
  }
  .brand__name {
    position: absolute;
    left: 142px;
    top: 32px;
    font-weight: 800;
    font-size: 52px;
    line-height: 1;
    letter-spacing: 1px;
    color: var(--text-white);
    white-space: nowrap;
  }
  .brand__tagline {
    position: absolute;
    left: 142px;
    top: 86px;
    font-weight: 700;
    font-size: 19px;
    color: var(--tagline-blue);
    white-space: nowrap;
  }
  .message {
    position: absolute;
    left: 534px;
    top: 144px;
    width: 586px;
    height: 600px;
    color: var(--text-white);
    text-align: center;
  }
  .message__headline {
    position: absolute;
    left: 0;
    top: 166px;
    width: 100%;
    font-weight: 300;
    font-stretch: 75%;
    font-size: 54px;
    line-height: 47px;
    letter-spacing: 0.5px;
  }
  .message__instruction {
    position: absolute;
    left: 69px;
    top: 318px;
    width: 450px;
    padding: 12px 0;
    border-top: 2px solid var(--text-white);
    border-bottom: 2px solid var(--text-white);
    font-weight: 600;
    font-size: 20px;
    line-height: 25px;
  }
  .message__url {
    position: absolute;
    left: 0;
    top: 499px;
    width: 100%;
    font-weight: 700;
    font-size: 27px;
    letter-spacing: 14px;
  }
  .postcard__waves {
    position: absolute;
    left: 0;
    bottom: 0;
    width: 1120px;
    height: 110px;
  }
</style>
</head>
<body>
  <main class="postcard">
    <div class="postcard__photo" role="img" aria-label="Close-up of a doctor in a white coat holding a stethoscope whose chest piece is a clock face"></div>

    <header class="postcard__header">
      <p class="brand__name">QELVARO</p>
      <p class="brand__tagline">Leaders in Healthcare Communication</p>
    </header>

    <section class="message">
      <h1 class="message__headline">SALES REPRESENTATIVE<br>RESTRICTIED OFFICE</h1>
      <p class="message__instruction">PICK UP SALE REPRESENTATIVE PACKET<br>AT FRONT DESK OR SIGN UP AT</p>
      <p class="message__url">www.qelvaro.com</p>
    </section>

    <svg class="postcard__waves" viewBox="0 0 1120 110" preserveAspectRatio="none" aria-hidden="true">
      <path d="M0 36 C 300 20, 520 52, 760 40 S 1020 20, 1120 24 L1120 110 L0 110 Z" fill="#ffffff"/>
      <path d="M0 42 C 300 28, 520 58, 760 46 S 1020 28, 1120 30 L1120 110 L0 110 Z" fill="var(--deep-navy)"/>
      <path d="M0 64 C 320 54, 560 70, 800 62 S 1040 52, 1120 56 L1120 72 C 1000 68, 820 76, 600 76 S 200 70, 0 80 Z" fill="var(--stripe-blue)"/>
      <path d="M0 88 C 300 84, 600 92, 880 88 S 1060 84, 1120 86 L1120 96 C 900 98, 600 100, 300 98 S 60 96, 0 98 Z" fill="var(--stripe-light)"/>
    </svg>
  </main>
</body>
</html>
```